Project Finance Brochure

We are a finance fund helping bring energy efficiency and clean energy projects into the world. We would like a professionally created back and front brochure. Please take our internally created piece and work your magic!

Target Market(s)

We are targeting building owners, hotel operators, manufacturing plant engineers.

Industry/Entity Type

Finance

Font styles to use
Sans Serif

Requirements
Must have
• Must be clear and easy to understand. Flow charts help.
Nice to have
• Colors, fonts.

```html
<!DOCTYPE html>
<html lang="en">
<head>
<meta charset="utf-8">
<title>Veridane Capital Partners – Back Cover</title>
<link rel="stylesheet" href="https://fonts.googleapis.com/css2?family=Cormorant+SC:wght@500;600&family=Lato:wght@300;400&display=swap">
<style>
  :root {
    --paper: #ffffff;
    --ink: #111111;
    --navy: #1f2777;
    --muted: #8a8a8a;
    --hex-deep: #3d5f9e;
    --hex-mid: #4f8fc4;
    --hex-light: #8db6da;
  }
  html, body {
    margin: 0;
    padding: 0;
    overflow: hidden;
    background: var(--paper);
  }
  .back-cover {
    position: relative;
    width: 848px;
    height: 1200px;
    overflow: hidden;
    background: var(--paper);
    font-family: "Lato", sans-serif;
    color: var(--ink);
  }
  .hex-field {
    position: absolute;
    left: 0;
    top: 0;
    width: 848px;
    height: 930px;
  }
  .contact-block {
    position: absolute;
    left: 425px;
    top: 757px;
  }
  .contact-heading {
    margin: 0 0 33px;
    font-family: "Cormorant SC", serif;
    font-weight: 600;
    font-size: 26px;
    line-height: 34px;
    letter-spacing: 0.5px;
    color: var(--ink);
  }
  .company-name {
    margin: 0;
    font-size: 21px;
    line-height: 28px;
    color: var(--navy);
  }
  .address-line {
    margin: 0;
    font-size: 21px;
    line-height: 28px;
  }
  .members {
    position: absolute;
    left: 51px;
    top: 1019px;
    font-size: 16px;
    line-height: 21px;
  }
  .members-title { margin: 0 0 26px; }
  .member-name { margin: 0; }
  .member-email { margin: 0; color: var(--muted); font-weight: 300; }
</style>
</head>
<body>
  <main class="back-cover">
    <svg class="hex-field" viewBox="0 0 848 930" role="img" aria-label="Overlapping translucent blue hexagon pattern">
      <defs>
        <linearGradient id="hexTone" x1="0" y1="0" x2="1" y2="1">
          <stop offset="0" stop-color="var(--hex-deep)"/>
          <stop offset="0.5" stop-color="var(--hex-mid)"/>
          <stop offset="1" stop-color="var(--hex-light)"/>
        </linearGradient>
      </defs>
      <polygon fill="url(#hexTone)"
        points="0,0 848,0 848,330 825,437 775,545 655,636 520,580 458,690 410,800 287,890 152,830 34,922 0,905"/>
    </svg>

    <section class="contact-block">
      <h2 class="contact-heading">If You Have A Project Please<br>Contact Us</h2>
      <p class="company-name">Veridane Capital Partners, LLC</p>
      <p class="address-line">410 Meridian Avenue Suite 120</p>
      <p class="address-line">Menlo Park, CA 94025</p>
      <p class="address-line">415-555-0147</p>
      <p class="address-line">www.veridane.com</p>
    </section>

    <section class="members">
      <p class="members-title">Managing Members:</p>
      <p class="member-name">Daniel Morita</p>
      <p class="member-email">dmorita@veridane.com</p>
      <p class="member-name">Julian Pablo Arce, CFA</p>
      <p class="member-email">jparce@veridane.com</p>
    </section>
  </main>
</body>
</html>
```